Korvo Suplies

Packaging design for Multitool Blades, something similar to the drawing on paper, diecut of the packaging attached

Logo Text

Korvo Supplies

```html
<!DOCTYPE html>
<html lang="en">
<head>
<meta charset="utf-8">
<title>Korvo Supplies – Multitool Blade Blister Card</title>
<link rel="stylesheet" href="https://fonts.googleapis.com/css2?family=Archivo+Black&family=Montserrat:wght@800&display=swap">
<style>
  :root {
    --page: #fdfdfd;
    --card: #1b1b1b;
    --card-deep: #080808;
    --green: #00ff0c;
    --green-shade: #00a808;
    --white: #ffffff;
    --ink: #0d0d0d;
    --wood: #7a5c3a;
    --wood-dark: #4e3820;
    --slate: #4f6272;
  }
  * { margin: 0; padding: 0; box-sizing: border-box; }
  html, body { width: 927px; height: 1200px; overflow: hidden; background: var(--page); }
  .canvas { position: relative; width: 927px; height: 1200px; }

  .card {
    position: absolute; left: 296px; top: 216px; width: 328px; height: 759px;
    border-radius: 22px; overflow: hidden;
    background:
      linear-gradient(140deg, var(--card-deep) 0%, #151515 30%, transparent 30.2%),
      linear-gradient(160deg, transparent 55%, var(--card-deep) 62%, #161616 70%, transparent 70.2%),
      linear-gradient(200deg, transparent 78%, #0b0b0b 86%, transparent 86.2%),
      var(--card);
  }

  .hang-hole { position: absolute; left: 100px; top: 21px; }

  .brand {
    position: absolute; left: 0; top: 120px; width: 100%;
    display: flex; align-items: center; justify-content: center; gap: 10px;
  }
  .brand-mark { width: 18px; height: 18px; background: var(--green); }
  .brand-name {
    font-family: "Archivo Black", sans-serif; font-size: 27px; line-height: 1;
    color: var(--white); letter-spacing: 1px; text-transform: uppercase;
  }

  .blade-window { position: absolute; left: 0; top: 0; }

  .materials {
    position: absolute; left: 260px; top: 234px; width: 47px;
    display: flex; flex-direction: column; gap: 13px;
  }
  .material { width: 47px; }
  .material-photo { width: 47px; height: 33px; border-radius: 5px 5px 0 0; }
  .material-photo.wood { background: linear-gradient(160deg, #fff 30%, var(--wood) 31%, var(--wood-dark)); }
  .material-photo.hardwood { background: linear-gradient(165deg, #fff 30%, #6a4a2c 31%, #3f2a16); }
  .material-photo.panel { background: linear-gradient(165deg, #fff 25%, var(--slate) 26%, var(--slate) 55%, #8a6a44 56%, #5a4026); }
  .material-label {
    display: block; background: #151515; color: var(--white);
    font-family: "Montserrat", sans-serif; font-weight: 800; font-size: 6px;
    text-align: center; padding: 2px 0 3px; border-radius: 0 0 5px 5px;
  }

  .hcs-badge {
    position: absolute; left: 263px; top: 423px; width: 42px; height: 42px;
    border-radius: 50%; background: var(--green); color: var(--ink);
    font-family: "Archivo Black", sans-serif; font-size: 13px;
    display: flex; align-items: center; justify-content: center;
  }

  .tagline {
    position: absolute; left: 27px; top: 717px;
    transform: rotate(-90deg); transform-origin: 0 0;
    font-family: "Archivo Black", sans-serif; font-style: italic; font-size: 25px;
    line-height: 1; color: var(--white); white-space: nowrap; letter-spacing: 0.5px;
  }
</style>
</head>
<body>
<main class="canvas">
  <section class="card">
    <svg class="hang-hole" width="128" height="48" viewBox="0 0 128 48" aria-hidden="true">
      <circle cx="64" cy="17" r="17" fill="var(--white)"/>
      <rect x="0" y="17" width="128" height="27" rx="13.5" fill="var(--white)"/>
    </svg>

    <div class="brand">
      <span class="brand-mark"></span>
      <span class="brand-name">Korvo Supplies</span>
    </div>

    <svg class="blade-window" width="328" height="759" viewBox="0 0 328 759" aria-hidden="true">
      <defs>
        <filter id="inset" x="-10%" y="-10%" width="120%" height="120%">
          <feFlood flood-color="#007a06"/>
          <feComposite in2="SourceAlpha" operator="out"/>
          <feGaussianBlur stdDeviation="6"/>
          <feComposite in2="SourceAlpha" operator="in"/>
          <feMerge><feMergeNode in="SourceGraphic"/><feMergeNode/></feMerge>
        </filter>
      </defs>
      <path filter="url(#inset)" fill="var(--green)"
        d="M92 293 L92 293 A72 72 0 0 1 236 293 L236 473 Q236 478 232 482 L218 497 Q215 500 215 505 L215 636 Q215 641 218 644 L262 688 Q266 692 266 697 L266 703 Q266 713 256 713 L74 713 Q64 713 64 703 L64 697 Q64 692 68 688 L110 646 Q113 643 113 638 L113 505 Q113 500 110 497 L96 482 Q92 478 92 473 Z"/>
    </svg>

    <div class="materials">
      <div class="material">
        <div class="material-photo wood" role="img" aria-label="Photo of wooden beams"></div>
        <span class="material-label">WOOD</span>
      </div>
      <div class="material">
        <div class="material-photo hardwood" role="img" aria-label="Photo of a hardwood plank"></div>
        <span class="material-label">HARDWOOD</span>
      </div>
      <div class="material">
        <div class="material-photo panel" role="img" aria-label="Photo of a laminated hardwood panel"></div>
        <span class="material-label">HARDWOOD</span>
      </div>
    </div>

    <div class="hcs-badge">HCS</div>

    <p class="tagline">HIGH QUALITY</p>
  </section>
</main>
</body>
</html>
```